Gigglewave Studio 3 fold Brochure

a 3-fold flyer on 8.5 x 11 glossy paper showing the benefits of laughter in your life. One side should be available for mailing:
Address:
Gigglewave Studio
4312 Marbury Lane
San Jose, CA 95847

other contact info:
Denise Prewitt
Certified Mirth Motion Teacher, CMMT, CMML
info@gigglewavestudio.example
http://gigglewavestudio.example/Home.html
www.social.example/gigglewavestudio
Blog: chucklemeadow.blog.example/
(408) 555-0187

Target Market(s)

non-profit organizations, medical field and corporations

Requirements
Must have
• colors as shown on the Gigglewave Studio web site. 3 fold flyer is to be double sided.
Should not have
• should not look too busy but needs to provide sufficient information

```html
<!DOCTYPE html>
<html lang="en">
<head>
<meta charset="utf-8">
<title>Gigglewave Studio – Tri-fold Brochure</title>
<link rel="stylesheet" href="https://fonts.googleapis.com/css2?family=Exo+2:ital,wght@0,600;0,700;0,800;1,700;1,800&display=swap">
<style>
  :root {
    --backdrop: #5e6163;
    --purple-deep: #5a2776;
    --purple-mid: #6c3790;
    --purple-light: #8b52a6;
    --lime: #c9d23a;
    --lime-pale: #eef0b8;
    --cyan: #27a6d2;
    --orange: #e9a23b;
    --orange-soft: #f2b25a;
    --violet: #7a3da0;
    --ink-purple: #3c1859;
    --paper: #ffffff;
  }
  * { box-sizing: border-box; margin: 0; padding: 0; }
  html, body { width: 1200px; height: 1000px; overflow: hidden; }
  body {
    background: var(--backdrop);
    font-family: "Exo 2", Arial, sans-serif;
    position: relative;
  }
  .brochure {
    position: absolute;
    left: 60px; top: 82px;
    width: 1080px; height: 835px;
    display: flex;
    box-shadow: 0 14px 40px rgba(0,0,0,.35);
  }
  .panel { position: relative; width: 360px; height: 100%; overflow: hidden; }
  .panel-top { position: absolute; left: 0; top: 0; width: 100%; height: 470px; }
  .panel-bottom { position: absolute; left: 0; top: 470px; width: 100%; height: 365px; }

  /* Cover panel */
  .cover .panel-top {
    background: linear-gradient(160deg, #d9df7a 0%, #eef0c8 45%, #f5f5ee 100%);
  }
  .cover .backdrop-photo {
    position: absolute; inset: 0;
    background: linear-gradient(150deg, rgba(201,210,58,.55), rgba(240,236,220,.6) 55%, rgba(255,255,255,.4));
  }
  .cover .frame { position: absolute; inset: 0; }
  .cover .feature-photo {
    position: absolute; left: 70px; top: 170px; width: 290px; height: 300px;
    background: linear-gradient(170deg, #4a4a4c 0%, #5b524a 50%, #8a6a4c 100%);
  }
  .cover .panel-bottom { background: var(--purple-deep); }
  .brand-mark {
    position: absolute; left: 0; right: 0; top: 150px;
    display: flex; align-items: center; justify-content: center; gap: 12px;
  }
  .brand-mark .dot { width: 16px; height: 16px; border-radius: 50%; background: var(--lime); }
  .brand-mark .name { color: var(--lime); font-weight: 800; font-size: 30px; letter-spacing: .5px; }

  /* Contact panel */
  .contact .panel-top {
    background: linear-gradient(180deg, #f3f1ee 0%, #e9e4e6 60%, #f6f4f5 100%);
  }
  .contact .faded-photo {
    position: absolute; inset: 0;
    background: linear-gradient(160deg, rgba(220,210,205,.7), rgba(245,243,240,.5) 60%, rgba(255,255,255,.8));
  }
  .contact .brand-faint {
    position: absolute; left: 0; right: 0; top: 300px; text-align: center;
    color: var(--purple-mid); font-weight: 800; font-size: 32px;
  }
  .contact .panel-bottom { background: var(--purple-mid); padding: 40px 34px 0; color: var(--paper); }
  .contact-title { font-weight: 700; font-size: 20px; letter-spacing: 6px; color: var(--paper); margin-bottom: 14px; }
  .contact-list { list-style: none; font-size: 14px; font-weight: 600; line-height: 1.75; }
  .contact-list .person { color: var(--cyan); font-weight: 700; }
  .contact-list .line { color: var(--lime); }
  .contact-phone { margin-top: 30px; font-size: 22px; letter-spacing: 4px; color: var(--paper); font-weight: 600; }

  /* Benefits / mailing panel */
  .mailing .panel-top {
    background: linear-gradient(180deg, #e7ec9a 0%, #f4f5d6 45%, #ffffff 100%);
  }
  .mailing .corner { position: absolute; right: 0; top: 0; }
  .benefits { list-style: none; position: absolute; left: 34px; right: 28px; top: 70px; }
  .benefits li { font-style: italic; font-weight: 800; font-size: 17px; line-height: 1.3; margin-bottom: 30px; }
  .benefits .b1 { color: var(--orange); }
  .benefits .b2 { color: var(--lime); }
  .benefits .b3 { color: var(--cyan); }
  .benefits .b4 { color: var(--violet); }
  .benefits .b5 { color: var(--ink-purple); }
  .mailing .panel-bottom { background: var(--purple-light); padding: 120px 40px 0; }
  .mail-address { font-style: italic; font-weight: 800; font-size: 24px; line-height: 1.9; }
  .mail-address .org { color: var(--paper); }
  .mail-address .street, .mail-address .city { color: var(--orange-soft); }

  .fold { position: absolute; top: 0; bottom: 0; width: 1px; background: rgba(0,0,0,.12); }
</style>
</head>
<body>
  <main class="brochure">
    <section class="panel cover">
      <div class="panel-top">
        <div class="backdrop-photo" role="img" aria-label="Faded photo of a smiling woman in glasses laughing"></div>
        <div class="feature-photo" role="img" aria-label="Photo of a laughing couple tossing autumn leaves"></div>
        <svg class="frame" width="360" height="470" viewBox="0 0 360 470" aria-hidden="true">
          <path d="M40 170 L70 170 L70 470 L40 470 Z" fill="#ffffff"/>
          <path d="M300 140 Q350 160 360 230 L360 140 Z" fill="#ffffff"/>
          <path d="M360 380 L360 470 L260 470 Z" fill="#27a6d2"/>
        </svg>
      </div>
      <div class="panel-bottom">
        <div class="brand-mark">
          <span class="dot"></span>
          <span class="name">Mirth Motion</span>
        </div>
      </div>
    </section>

    <section class="panel contact">
      <div class="panel-top">
        <div class="faded-photo" role="img" aria-label="Faded photo of a woman laughing"></div>
        <div class="brand-faint">Mirth Motion</div>
      </div>
      <div class="panel-bottom">
        <h2 class="contact-title">CONTACT</h2>
        <ul class="contact-list">
          <li class="person">Denise Prewitt</li>
          <li class="line">Certified Mirth Motion Teacher, CMMT, CMML</li>
          <li class="line">info@gigglewavestudio.example</li>
          <li class="line">http://gigglewavestudio.example/Home.html</li>
          <li class="line">www.social.example/gigglewavestudio</li>
          <li class="line">Blog: chucklemeadow.blog.example/</li>
        </ul>
        <p class="contact-phone">(408) 555-0187</p>
      </div>
      <span class="fold" style="left:0"></span>
    </section>

    <section class="panel mailing">
      <div class="panel-top">
        <svg class="corner" width="120" height="60" viewBox="0 0 120 60" aria-hidden="true">
          <path d="M30 0 L120 0 L120 60 Z" fill="#27a6d2"/>
        </svg>
        <ul class="benefits">
          <li class="b1">Fun and Relaxed Exercise for Wellness and Happiness</li>
          <li class="b2">Instant Stress-Reliever to Improve Immune System</li>
          <li class="b3">Keeps You in A Cheerful Mood Through the Day</li>
          <li class="b4">Oxygenates Brain and Body to Make You Feel Energized</li>
          <li class="b5">Promotes a Positive Outlook in Life, Especially in Trying Times</li>
        </ul>
      </div>
      <div class="panel-bottom">
        <address class="mail-address">
          <div class="org">Gigglewave Studio</div>
          <div class="street">4312 Marbury Lane</div>
          <div class="city">San Jose, CA 95847</div>
        </address>
      </div>
      <span class="fold" style="left:0"></span>
    </section>
  </main>
</body>
</html>
```